we are an outdoor outlet in a country club that has a variety of outlets. The Club is called Brindlewood and is located in Cairo, Egypt. This garden menu will include cuisines from the Mediterranean, Asia and Texmex. we need a menu that is colorful and would fit an A3 size, back and front are to be used. Attached is the old menu currently in use (Garden Menu 2012.pdf is just for reference) and the new menu text for you to use is under the name Garden Menu Fall 2013
thank you.

```html
<!DOCTYPE html>
<html lang="en">
<head>
<meta charset="utf-8">
<title>Brindlewood Garden Menu</title>
<link rel="stylesheet" href="https://fonts.googleapis.com/css2?family=Roboto+Condensed:wght@400;700&family=Pinyon+Script&display=swap">
<style>
:root{
  --stage:#e6e6e6;
  --lime:#a6c84a;
  --leaf:#7a9e2a;
  --tomato:#c41e22;
  --ink-light:#ffffff;
  --ink-dark:#3a3a2a;
  --brand:#6b3a2a;
}
*{margin:0;padding:0;box-sizing:border-box}
html,body{width:1200px;height:900px;overflow:hidden}
body{background:var(--stage);font-family:"Roboto Condensed",Arial,sans-serif;color:var(--ink-light)}
.spread{position:relative;width:1200px;height:900px}
.panel{position:absolute;top:130px;width:360px;height:640px;box-shadow:0 6px 18px rgba(0,0,0,.18);overflow:hidden}
.panel-bg{position:absolute;inset:0;width:100%;height:100%}
.cover{left:30px;background:#fff}
.page-red{left:420px;background:transparent;box-shadow:none}
.page-green{left:810px;background:var(--lime)}
.cover-title{position:absolute;top:150px;left:0;width:100%;text-align:center;font-family:"Pinyon Script",cursive;color:var(--ink-dark);font-size:40px;line-height:.9}
.hat-emblem{position:absolute;top:95px;left:160px;width:42px;height:42px;border-radius:50%;background:rgba(255,255,255,.35)}
.brand{position:absolute;bottom:70px;left:0;width:100%;display:flex;justify-content:center;align-items:center;gap:8px}
.brand-dot{width:14px;height:14px;border-radius:50%;background:var(--leaf)}
.brand-name{font-size:26px;font-weight:400;color:var(--brand)}
.columns{position:absolute;top:100px;left:18px;right:18px;bottom:20px;display:flex;gap:12px}
.col{flex:1;display:flex;flex-direction:column}
.col + .col{border-left:1px solid rgba(255,255,255,.55);padding-left:12px}
.section{font-weight:700;font-size:12px;text-transform:uppercase;text-align:center;margin:8px 0 5px}
.sub{font-weight:700;font-size:10px;margin:4px 0 2px}
.item{margin-bottom:4px}
.item-name{font-size:10px;font-weight:400;line-height:1.15}
.item-desc{font-size:7px;line-height:1.2;opacity:.92}
.plain{font-size:9.5px;line-height:1.3}
</style>
</head>
<body>
<main class="spread">

  <section class="panel cover">
    <svg class="panel-bg" viewBox="0 0 360 640" preserveAspectRatio="none">
      <defs>
        <linearGradient id="coverFade" x1="0" y1="0" x2="0" y2="1">
          <stop offset="0" stop-color="#9cc03e"/>
          <stop offset=".55" stop-color="#ffffff"/>
          <stop offset="1" stop-color="#ffffff"/>
        </linearGradient>
      </defs>
      <rect width="360" height="120" fill="#8fb238"/>
      <path d="M0,80 Q180,55 360,80 V640 H0Z" fill="url(#coverFade)"/>
    </svg>
    <div class="hat-emblem" role="img" aria-label="Chef hat emblem"></div>
    <h1 class="cover-title">Menu<br>Card</h1>
    <div class="brand"><span class="brand-dot"></span><span class="brand-name">Brindlewood</span></div>
  </section>

  <section class="panel page-red">
    <svg class="panel-bg" viewBox="0 0 360 640" preserveAspectRatio="none">
      <path d="M0,60 Q180,30 360,60 V640 H0Z" fill="var(--tomato)"/>
    </svg>
    <div class="columns">
      <div class="col">
        <h2 class="section">Soups</h2>
        <div class="item"><p class="item-name">Lentil soup</p><p class="item-desc">with lemon and cumin</p></div>
        <div class="item"><p class="item-name">Cream of chicken</p><p class="item-desc">with croutons</p></div>
        <div class="item"><p class="item-name">Tomato soup</p><p class="item-desc">with fresh basil</p></div>
        <h2 class="section">Appetizers</h2>
        <div class="item"><p class="item-name">Falafel platters</p><p class="item-desc">with lemon juice, garlic, and black pepper</p></div>
        <div class="item"><p class="item-name">Fried eggplant rolls</p><p class="item-desc">stuffed ricotta cheese and pine nuts</p></div>
        <div class="item"><p class="item-name">Kofta in mini pita</p><p class="item-desc">with tehina and oriental salsa</p></div>
        <div class="item"><p class="item-name">Manakousha</p><p class="item-desc">with thyme and olive oil</p></div>
        <div class="item"><p class="item-name">Fried kebeba</p><p class="item-desc">with minced meat, spices, and pine nuts</p></div>
        <div class="item"><p class="item-name">Fried calamari a la Romana</p><p class="item-desc">served with aioli</p></div>
        <div class="item"><p class="item-name">Sambousek</p><p class="item-desc">with herbed white cheese and mint</p></div>
        <div class="item"><p class="item-name">Oriental sausage</p><p class="item-desc">sautéed with garlic and onion</p></div>
        <div class="item"><p class="item-name">Mini vine leaves</p><p class="item-desc">with a yoghurt dip</p></div>
        <div class="item"><p class="item-name">Fattoush</p><p class="item-desc">with a pomegranate syrup dressing</p></div>
        <div class="item"><p class="item-name">Hummus seasoned</p><p class="item-desc">with lemon juice, garlic, and olive oil</p></div>
        <div class="item"><p class="item-name">White cheese</p><p class="item-desc">with diced tomato, thyme, and olive oil</p></div>
        <div class="item"><p class="item-name">Tehina</p><p class="item-desc">seasoned with cumin, lemon juice, and garlic</p></div>
      </div>
      <div class="col">
        <h2 class="section">Salads</h2>
        <div class="item"><p class="item-name">Caprese</p><p class="item-desc">Buffalo mozzarella and sliced tomato with a balsamic vinaigrette</p></div>
        <div class="item"><p class="item-name">Rocket Apple</p><p class="item-desc">Rocket leaves with gorgonzola, croutons, and strawberry vinaigrette</p></div>
        <div class="item"><p class="item-name">French Riviera Nicoise</p><p class="item-desc">Lettuce, egg, tomato, tuna, olives, onion, celery, radish, bell pepper in a French vinaigrette</p></div>
        <div class="item"><p class="item-name">Folle</p><p class="item-desc">Mixed greens with crab sticks, mushroom, corn, cherry tomato in a mango vinaigrette</p></div>
        <h2 class="section">Pizza &amp; Pasta</h2>
        <div class="item"><p class="item-name">Pizza Margarita (Choose your toppings)</p></div>
        <div class="item"><p class="item-name">Create your own pasta</p><p class="item-desc">Type: Spaghetti, Tagliatelle, Penne<br>Sauces: Napolitaine, Bolognese, Alfredo</p></div>
        <h2 class="section">Toppings</h2>
        <p class="item-desc">Bell peppers, olives, tomato, onion<br>Mushroom, chicken, tuna, pepperoni<br>Smoked salmon, shrimps<br>Lasagna</p>
        <h2 class="section">Sandwiches</h2>
        <p class="item-desc">(Served with French fries or a garden salad)<br>Beef or chicken Shawerma</p>
        <div class="item"><p class="item-name">Grilled kofta</p><p class="item-desc">Greek lamb gyro in pita bread with Tzatziki<br>Club sandwich with smoked beef, turkey, egg</p></div>
        <h2 class="section">Main Courses</h2>
        <div class="item"><p class="item-name">Veal Parmeggiana</p><p class="item-desc">Breaded veal escalope topped with melted cheese and tomato sauce served with Spaghetti</p></div>
        <div class="item"><p class="item-name">Chicken a la Francaise</p><p class="item-desc">Pan fried chicken breast in a mushroom cream sauce with vegetables white rice</p></div>
      </div>
    </div>
  </section>

  <section class="panel page-green">
    <svg class="panel-bg" viewBox="0 0 360 640" preserveAspectRatio="none">
      <path d="M0,60 Q180,30 360,60 V640 H0Z" fill="var(--leaf)"/>
    </svg>
    <div class="columns">
      <div class="col">
        <div class="item"><p class="item-name">Grilled Salmon</p><p class="item-desc">Salmon steak charcoal grilled with avocado tomato salsa and creamy mushroom risotto</p></div>
        <div class="item"><p class="item-name">Moroccan Chicken</p><p class="item-desc">Chicken cubes simmered with spices and olives served with tomato rice</p></div>
        <div class="item"><p class="item-name">Filet</p><p class="item-desc">Tender filet grilled to your liking served with mashed potato and creamed spinach</p></div>
        <div class="item"><p class="item-name">Choice of sauces</p><p class="item-desc">Brown mushroom, Green Peppercorn, Gorgonzola</p></div>
        <h2 class="section">Asian Corner</h2>
        <p class="sub">Salads &amp; Appetizers:</p>
        <div class="item"><p class="item-name">Chicken Wasabi Salad</p><p class="item-desc">Diced chicken with a mayo wasabi dressing on top of shredded lettuce</p></div>
        <div class="item"><p class="item-name">Chicken Sesame Noodle Salad</p><p class="item-desc">Sesame crusted chicken with glass noodles tossed with sweet chili, soy sauce, and lemongrass</p></div>
        <div class="item"><p class="item-name">Spring rolls</p><p class="item-desc">Vegetable spring rolls served with house made sweet and sour dip</p></div>
        <div class="item"><p class="item-name">Indian Samosa</p><p class="item-desc">Fried dough parcels filled with vegetables and spices</p></div>
        <p class="sub">Main Courses:</p>
        <div class="item"><p class="item-name">Murgh Chicken Makhni</p><p class="item-desc">Chicken cubes in a rich creamy tomato sauce seasoned with garam masala</p></div>
        <div class="item"><p class="item-name">Choice of side</p><p class="item-desc">vegetable korma or curd</p></div>
        <div class="item"><p class="item-name">Chicken Tandoori</p><p class="item-desc">Grilled chicken cubes with tandoori spices served with basmati rice</p></div>
        <div class="item"><p class="item-name">Thai Coconut Curry Shrimp</p><p class="item-desc">Sautéed shrimp tossed with curry and coconut milk served with jasmine rice</p></div>
        <div class="item"><p class="item-name">Mongolian Beef</p><p class="item-desc">Soy marinated beef with oyster sauce and vegetables served with egg noodles</p></div>
      </div>
      <div class="col">
        <h2 class="section">Tex Mex</h2>
        <p class="sub">Salads &amp; Appetizers:</p>
        <div class="item"><p class="item-name">Caesar Salad</p><p class="item-desc">Iceberg lettuce with Caesar dressing with grated Parmesan cheese and croutons</p></div>
        <div class="item"><p class="item-name">Taco salad</p><p class="item-desc">Chicken breast, beans, sour cream, guacamole, tomato, corn, lettuce, olives, onion, vinaigrette<br>Nachos topped with chili, melted cheese, beans<br>Chicken Quesadilla served with guacamole, salsa, and sour cream</p></div>
        <p class="sub">Main Courses &amp; Sandwiches:</p>
        <div class="item"><p class="item-name">Cheeseburger</p><p class="item-desc">House made beef burger topped with cheddar cheese</p></div>
        <div class="item"><p class="item-name">Mushroom Burger</p><p class="item-desc">Beef burger with sautéed mushroom, caramelized onion, and provolone cheese</p></div>
        <div class="item"><p class="item-name">Crispy Chicken Wrap</p><p class="item-desc">Crisp fried chicken wrap with a ranch dressing<br>Fajita (Chicken, Beef, Combo)</p></div>
        <div class="item"><p class="item-desc">Pan seared meat or chicken with onion and bell pepper served with sour cream, guacamole, salsa</p></div>
        <h2 class="section">Desserts</h2>
        <p class="plain">Mix Berries Cheesecake<br>Crème Brulee<br>Chocolate Caramel Cake<br>Warm Chocolate Fondant<br>Baked Apple Tart Tatin<br>Tiramisu<br>Pumpkin Pie Flan<br>Mixed Berries Granola Yoghurt<br>Vanilla Ice Cream Profiterole with dark and white chocolate sauce<br>Caramelized Banana with Deep Fried Ice Cream<br>Baklava with Nuts and Sugar Syrup<br>Shot Glass Sampler – Tiramisu, Chocolate Crisp Mousse, Pear with Sabayon<br>Ice Cream by Scoop</p>
      </div>
    </div>
  </section>

</main>
</body>
</html>
```